Webdesign für eine Softwarewarentwicklung und Consulting für das Gesundheitswesen
Zielgruppe
Softwarewarentwicklung und Consulting für das Gesundheitswesen. Unsere Zielgruppe sind Unternehmen und Organisationen im Bereich des Gesundheitswesen. Weiter informationen auf derzeitiger Homepage unter www.vmt-pflegeloesung.de.
Aufgabenstellung
Das Webdesign sollte deutlich moderner und kreativer wirken als unsere derzeitige Hompage. (Die bisherige Hompage wurde seinerzeit bei der Gründung 'auf die Schnelle' entwickelt.) Die neue Homapage sollte 'frisch' wirken und einem modernen Softwareunternehmen entsprechen.: Schlicht, modern und innovativ. Die Website sollte auch später gut auf Handy und Tablet darstellbar sein. Da wir derzeit wenig Inhalte auf unserer Homepage haben, wären wir auch für inhaltliche Vorschläge dankbar. Unsere Logofarben sollten sich auch im Design wiederfinden (der Rotton hat den Wert RGB: 227, 7, 19 #e30713 - der Blauton hat den Wert RGB: 30, 38, 74 1 #e264a).
Im Format bin ich unerfahren und würde dann für das spätere Umsetzen Adobe Photoshop vorschlagen.
Idealerweise sollte sich das Design später in einem gängigen CMS umsetzen lassen.
Gerne können Sie uns auch ein Komplettangebot auch zum Thema Umsetzung unterbreiten.
Grundsätzlich finde ich folgende Hompages ganz gut:
https://brelvuno.com/
https://www.kiesfeld.de/
https://www.plumvantic.com/de/
https://zirkanu.de/

```html
<!DOCTYPE html>
<html lang="de">
<head>
<meta charset="utf-8">
<title>VMT – Digitale Zukunftslösungen</title>
<link href="https://fonts.googleapis.com/css2?family=Montserrat:wght@300;400;500;600;700&display=swap" rel="stylesheet">
<style>
:root{
  --navy:#1e264a;
  --red:#e30713;
  --pink:#e2074c;
  --teal:#1f5f73;
  --grey:#7a7a7a;
  --line:#c9d6e3;
  --stage:#f1f2f4;
  --white:#ffffff;
}
*{margin:0;padding:0;box-sizing:border-box}
html,body{width:1200px;height:1200px;overflow:hidden;background:var(--stage);font-family:'Montserrat',sans-serif}
.page{position:absolute;left:437px;top:0;width:524px;height:1932px;background:var(--white);transform:scale(0.6211);transform-origin:0 0;box-shadow:0 0 30px rgba(0,0,0,.12);overflow:hidden}
.abs{position:absolute}
.topbar{left:0;top:0;width:524px;height:38px}
.brand{left:38px;top:8px;font-size:18px;font-weight:700;color:var(--navy);letter-spacing:.5px;display:flex;align-items:center;gap:4px}
.brand-dot{width:6px;height:6px;background:var(--red)}
.top-contact{top:14px;font-size:5px;color:var(--grey)}
.nav{left:0;top:38px;width:524px;height:39px;background:var(--navy);display:flex;justify-content:center;align-items:center;gap:20px;padding-left:0}
.nav a{color:var(--white);font-size:9.5px;text-decoration:none;font-weight:400}
.nav a.active{color:var(--red)}
.hero{left:0;top:77px;width:524px;height:170px;background:linear-gradient(100deg,#c9d8e6 0%,#aebfd0 35%,#6f8094 65%,#3b4658 100%)}
.section-title{color:var(--pink);font-size:11.5px;font-weight:400}
.intro{left:0;top:282px;width:524px;text-align:center}
.intro p{width:320px;margin:8px auto 0;font-size:6px;line-height:9.5px;color:var(--grey);font-weight:300}
.tile{width:92px;height:112px;background:var(--navy);border-radius:3px;color:var(--white);padding:15px 9px 0 10px}
.tile.accent{background:var(--pink)}
.tile h3{font-size:7px;font-weight:500;margin-bottom:4px}
.tile p{font-size:6px;line-height:9.7px;font-weight:300;color:#d9dbe5}
.photo{border-radius:2px}
.feature h2{margin-bottom:8px}
.feature p{font-size:6px;line-height:9.7px;color:#555;font-weight:300}
.service{width:116px;height:138px;border:1px solid var(--line);border-radius:3px;text-align:center;padding-top:10px}
.service svg{width:40px;height:40px}
.service h4{font-size:9px;font-weight:400;color:#555;margin:4px 0 12px}
.service p{font-size:6px;line-height:9.7px;color:var(--grey);font-weight:300;padding:0 3px}
.cta{left:0;top:1386px;width:524px;height:67px;background:var(--teal);color:var(--white)}
.cta-text{left:38px;top:30px;font-size:9.5px;font-weight:300}
.cta-phone{left:336px;top:14px;font-size:9px;font-weight:300}
.cta-btn{left:335px;top:35px;width:116px;height:20px;border-radius:10px;background:var(--pink);font-size:8.5px;font-weight:500;display:flex;align-items:center;justify-content:center}
.reviews{left:0;top:1453px;width:524px;height:316px;background:linear-gradient(135deg,#f4f7fa 0%,#e6eef5 45%,#f7f9fb 100%)}
.reviews-head{top:40px;left:0;width:524px;text-align:center}
.reviews-head p{width:330px;margin:7px auto 0;font-size:6px;line-height:8.7px;color:var(--grey);font-weight:300}
.quote{width:116px;height:138px;border:1px solid var(--line);border-radius:3px;background:rgba(255,255,255,.7);text-align:center;padding:34px 6px 0}
.quote p{font-size:6px;line-height:8.7px;color:var(--grey);font-weight:300}
.quote span{display:block;margin-top:16px;font-size:5px;color:#666;font-weight:500}
.footer{left:0;top:1769px;width:524px;height:163px;background:var(--navy);color:var(--white)}
.footer h5{position:absolute;left:66px;top:46px;font-size:10px;font-weight:300}
.footer p{position:absolute;font-size:6px;line-height:12.5px;font-weight:300;color:#d6d8e2}
</style>
</head>
<body>
<div class="page">
  <header class="abs topbar">
    <div class="abs brand">VMT<span class="brand-dot"></span></div>
    <div class="abs top-contact" style="left:324px">+49 30 55 / 4 12 77 -00</div>
    <div class="abs top-contact" style="left:408px">info@vmt-pflegeloesung.de</div>
  </header>
  <nav class="abs nav">
    <a class="active">Home</a><a>Produkte</a><a>Über uns</a><a>Jobangebote</a><a>Kontakt</a>
  </nav>
  <div class="abs hero" role="img" aria-label="Foto: Hände mit Smartphone am Laptop, Stethoskop auf dem Schreibtisch"></div>

  <section class="abs intro">
    <h1 class="section-title">Digitale Zukunftslösungen</h1>
    <p>Mit höchster Fachkompetenz im IT-Bereich, ist es unser Ziel, Ihr Unternehmen erfolgreich im digitalen Wandel des Gesundheitswesens zu positionieren. Wir entwickeln Strategien und Softwarelösungen, die genau auf Ihr Unternehmen zugeschnitten sind.</p>
  </section>

  <div class="abs tile" style="left:94px;top:386px"><h3>Prozessoptimierung</h3><p>Optimieren Sie Ihre Prozesse und steigern damit effizientes Arbeiten. Wir bieten Komplettlösungen.</p></div>
  <div class="abs tile accent" style="left:216px;top:386px"><h3>Digitalisierung</h3><p>Einfache Digitalisierung Ihrer Abläufe sowie Datenkontrolle.</p></div>
  <div class="abs tile" style="left:341px;top:386px"><h3>Onlineanwendung</h3><p>Wir stellen eine Vielzahl von Anwendungen bereit, damit Sie sich auf das wesentliche konzentrieren können.</p></div>
  <div class="abs tile" style="left:96px;top:527px"><h3>eRezept/E-Health</h3><p>Einfache digitale Übertragung der Rezepte und Online Gesundheitsberatung.</p></div>
  <div class="abs tile" style="left:216px;top:527px"><h3>Consulting</h3><p>Lorem ipsum dolor sit amet, consectetur adipiscing elit, sed do eiusmod tempor incididunt ut labore et dolore magna aliqua.</p></div>
  <div class="abs tile" style="left:342px;top:527px"><h3>Projektmanagement</h3><p>Lorem ipsum dolor sit amet, consectetur adipiscing elit.</p></div>

  <div class="abs photo" style="left:38px;top:736px;width:221px;height:139px;background:linear-gradient(90deg,#9fb0a4 0%,#dfe3e0 45%,#c99a86 75%,#b32533 100%)" role="img" aria-label="Foto: Ärztin mit Tablet im Gespräch mit einer Patientin"></div>
  <div class="abs feature" style="left:263px;top:736px;width:220px">
    <h2 class="section-title">Warum VMT</h2>
    <p>Lorem ipsum dolor sit amet, consectetur adipiscing elit, sed do eiusmod tempor incididunt ut labore et dolore magna aliqua. Ut enim ad minim veniam, quis nostrud exercitation ullamco laboris nisi ut aliquip ex ea commodo consequat. Duis aute irure dolor in reprehenderit in voluptate velit esse cillum dolore eu fugiat nulla pariatur. Excepteur sint occaecat cupidatat non proident, sunt in culpa qui officia deserunt mollit anim id est laborum. Lorem ipsum dolor sit amet, consectetur adipiscing elit, sed do eiusmod tempor incididunt ut labore et dolore magna aliqua. Ut enim ad minim veniam, quis nostrud exercitation ullamco laboris nisi ut aliquip ex ea commodo consequat.</p>
  </div>

  <div class="abs feature" style="left:38px;top:929px;width:219px">
    <h2 class="section-title">Unsere Lösungen für mehr Effizienz</h2>
    <p>Lorem ipsum dolor sit amet, consectetur adipiscing elit, sed do eiusmod tempor incididunt ut labore et dolore magna aliqua. Ut enim ad minim veniam, quis nostrud exercitation ullamco laboris nisi ut aliquip ex ea commodo consequat. Duis aute irure dolor in reprehenderit in voluptate velit esse cillum dolore eu fugiat nulla pariatur. Excepteur sint occaecat cupidatat non proident, sunt in culpa qui officia deserunt mollit anim id est laborum.</p>
  </div>
  <div class="abs photo" style="left:264px;top:902px;width:221px;height:139px;background:linear-gradient(135deg,#8a96a8 0%,#d8dde4 40%,#eef0f2 65%,#e6b77a 100%)" role="img" aria-label="Foto: Hände am Laptop mit Unterlagen, Diagrammen und Stethoskop"></div>

  <div class="abs service" style="left:72px;top:1117px">
    <svg viewBox="0 0 40 40" fill="none" stroke="#6d6d6d" stroke-width="3.2" stroke-linecap="round"><path d="M8 24v-5a12 12 0 0 1 24 0v5"/><rect x="6" y="21" width="6" height="10" rx="2" fill="#6d6d6d" stroke="none"/><rect x="28" y="21" width="6" height="10" rx="2" fill="#6d6d6d" stroke="none"/><path d="M31 31c0 4-4 5-9 5"/></svg>
    <h4>Beratung</h4><p>Wir beraten Sie und finden die passenden Lösungen zu Ihrem Business.</p>
  </div>
  <div class="abs service" style="left:203px;top:1117px">
    <svg viewBox="0 0 40 40" fill="none" stroke="#6d6d6d" stroke-width="3.2" stroke-linecap="round"><path d="M33 20a13 13 0 1 1-4-9.4"/><path d="M30 4v7h-7"/><path d="M16 16c2 4 4 6 8 8l2-2 3 2-2 3c-6-1-11-6-12-12l3-2 2 3z" fill="#6d6d6d" stroke="none"/></svg>
    <h4>Support</h4><p>Wir unterstützen Sie bei der Umsetzung und Ihren Fragen.</p>
  </div>
  <div class="abs service" style="left:335px;top:1117px">
    <svg viewBox="0 0 40 40" fill="none" stroke="#6d6d6d" stroke-width="3.2" stroke-linecap="round"><circle cx="20" cy="20" r="11"/><path d="M20 4v5M20 31v5M4 20h5M31 20h5M8.7 8.7l3.5 3.5M27.8 27.8l3.5 3.5M8.7 31.3l3.5-3.5M27.8 12.2l3.5-3.5"/><path d="M15 16a5 5 0 0 0 8 6l4 5"/></svg>
    <h4>Wartung</h4><p>Wir stehen Ihnen bei Problemen zur Seite. Sie haben immer einen Ansprechpartner.</p>
  </div>

  <section class="abs cta">
    <div class="abs cta-text">Haben Sie Fragen?&nbsp; Kontaktieren Sie uns!</div>
    <div class="abs cta-phone">+49 30 55 / 4 12 77 -00</div>
    <div class="abs cta-btn">Kontaktformular</div>
  </section>

  <section class="abs reviews" role="img" aria-label="Heller Hintergrund mit zarter Molekülstruktur">
    <div class="abs reviews-head">
      <h2 class="section-title">Was unsere Kunden sagen</h2>
      <p>Lorem ipsum dolor sit amet, consectetur adipiscing elit, sed do eiusmod tempor incididunt ut labore et dolore magna aliqua. Ut enim ad minim veniam, quis nostrud exercitation ullamco laboris nisi ut aliquip ex ea commodo consequat. Duis aute irure dolor in reprehenderit in voluptate velit esse cillum dolore eu fugiat nulla pariatur. Excepteur sint occaecat cupidatat non proident, sunt in culpa qui officia deserunt mollit anim id est laborum.</p>
    </div>
    <div class="abs quote" style="left:70px;top:137px"><p>Lorem ipsum dolor sit amet, consectetur adipiscing elit, sed do eiusmod tempor incididunt ut labore et dolore magna aliqua.</p><span>Max Mustermann</span></div>
    <div class="abs quote" style="left:197px;top:137px"><p>Lorem ipsum dolor sit amet, consectetur adipiscing elit, sed do eiusmod tempor incididunt ut labore et dolore magna aliqua.</p><span>Jana Roth</span></div>
    <div class="abs quote" style="left:327px;top:137px"><p>Lorem ipsum dolor sit amet, consectetur adipiscing elit, sed do eiusmod tempor incididunt ut labore et dolore magna aliqua.</p><span>Tim Weller</span></div>
  </section>

  <footer class="abs footer">
    <h5>VMT AG</h5>
    <p style="left:66px;top:68px">Birkenweg 12<br>40210 Lindenfeld</p>
    <p style="left:215px;top:59px">+49 30 55 / 4 12 77 -00<br>info@vmt-pflegeloesung.de<br>www.vmt-pflegeloesung.de</p>
    <p style="left:416px;top:68px">Impressum<br>Datenschutz</p>
  </footer>
</div>
</body>
</html>
```